Golden Years Mobile Massage Business Needs a New Website

Hello,
We require a website to be designed and coded. The design and coding must be high quality. Our website host has requested files be in static HTML format if possible.

The business is a mobile massage service for seniors (elderly people). The designer should emphasise that the business is a mobile service

The website will only have 4 pages.

1. Home- very simple layout and minimal information
2. Massage Services- this houses all of the information about the different services etc.
3. Contact Us-
4. ホーム (this is the Japanese symbol for 'home')- All of the information on the home page (section 1) will be translated into Japanese and uploaded to the brief for the designers to insert.

There is no requirement for an online booking, just contact information. The words 'Make a Booking' can be used and should lead customers to the 'Contact Us' page.

I have attached the business logo in multiple formats for designers to use.

I will upload more content and images to use for the website by the end of this week.

Thank you. I look forward to working with the successful candidate.

Target Market(s)

People aged 50+ years

Industry/Entity Type

Massage Therapy

Coding

Coded - Design and coding required

Number of Pages Required

4 page

Font styles to use
Sans Serif

Colors
74cabd
abd036
9ccb3b
f6faec
ffffff

Requirements
Must have
• Copyright free images and photos that we have taken. Both are important.
• Simple and inviting design.
Nice to have
• Colours of the logo incorporated.
Should not have
• This business is not a massage shop, so no images of massage shops or day salons required.
• Not too much imagery as the design needs to be simple.

```html
<!DOCTYPE html>
<html lang="en">
<head>
<meta charset="utf-8">
<title>Golden Years Mobile Massage</title>
<link href="https://fonts.googleapis.com/css2?family=Exo+2:wght@400;500;600;700&display=swap" rel="stylesheet">
<style>
:root{
  --black:#000000;
  --charcoal:#1a1a1a;
  --green:#9ccb3b;
  --lime:#abd036;
  --teal:#74cabd;
  --white:#ffffff;
  --mist:#f2f2f2;
  --grey-text:#8a8a8a;
  --dim-text:#6f6f6f;
}
*{margin:0;padding:0;box-sizing:border-box}
html,body{width:1200px;height:2278px;overflow:hidden}
body{font-family:"Exo 2",sans-serif;background:var(--white);color:var(--charcoal)}

.site-header{height:80px;background:var(--black);display:flex;align-items:center;justify-content:space-between;padding:0 70px 0 40px}
.brand{display:flex;align-items:center;gap:10px;color:var(--green);font-size:18px;font-weight:500;letter-spacing:.5px}
.brand-mark{width:12px;height:12px;background:var(--green);border-radius:50%}
.main-nav{display:flex;align-items:center;gap:20px}
.main-nav a{color:var(--green);text-decoration:none;font-size:12px;font-weight:700;letter-spacing:.3px}
.search-btn{width:28px;height:28px;border:1px solid #333;display:flex;align-items:center;justify-content:center}

.hero{height:763px;background:linear-gradient(120deg,#6e4a38 0%,#b57f62 35%,#caa084 60%,#e6d6c6 85%,#f2ece4 100%)}

.features{height:367px;display:flex;gap:73px;padding:56px 23px 0}
.feature-card{width:337px;height:284px;text-align:center;padding-top:48px}
.feature-card.light{background:linear-gradient(180deg,#e9e9e9,#dcdcdc)}
.feature-card.dark{background:var(--charcoal)}
.eyebrow{color:var(--green);font-size:12px;letter-spacing:.5px;text-transform:uppercase}
.feature-title{font-size:21px;font-weight:500;letter-spacing:.5px;margin:8px 0 14px}
.feature-card.light .feature-title{color:var(--charcoal)}
.feature-card.dark .feature-title{color:var(--white)}
.feature-text{font-size:12px;line-height:20px;color:var(--dim-text);padding:0 30px}
.btn{position:relative;display:inline-block;background:var(--green);color:var(--white);font-size:10px;font-weight:600;text-transform:uppercase;text-decoration:none;width:152px;height:36px;line-height:36px;margin-top:22px}
.btn::after{content:"";position:absolute;right:0;bottom:0;width:24px;height:3px;background:var(--teal)}

.services{height:542px;background:var(--black);text-align:center;padding-top:90px}
.section-title{font-size:28px;font-weight:500;letter-spacing:.5px;margin-top:6px}
.services .section-title{color:var(--white)}
.rule{width:1054px;margin:12px auto 0;height:1px;background:#888}
.service-grid{display:flex;gap:96px;padding:26px 73px 0}
.service{width:264px;text-align:center}
.service-photo{width:264px;height:175px;background:linear-gradient(180deg,#cfd6d4 0%,#7c8f6a 55%,#e8e8e8 75%,#cfcfcf 100%)}
.service-name{color:var(--white);font-size:12px;font-weight:600;margin-top:34px}
.service-text{font-size:12px;line-height:19px;color:#9a7c6a;width:334px;margin:8px 0 0 0}

.contact-head{height:185px;text-align:center;padding-top:88px}
.contact-head .rule{background:#eee}

.contact-split{height:269px;display:flex}
.contact-info{width:600px;background:var(--charcoal);text-align:center;padding-top:56px}
.contact-info .feature-title{color:var(--white);margin:6px 0 18px}
.contact-info p{font-size:12px;line-height:20px;color:var(--dim-text)}
.contact-info .lead{padding:0 50px;margin-bottom:10px}
.contact-info strong{color:var(--white);font-weight:500}
.quick-support{flex:1;background:var(--mist);text-align:center;padding-top:65px}
.quick-support .feature-title{color:var(--charcoal);margin:6px 0 14px}
.quick-support p{font-size:12px;color:var(--dim-text)}
.quick-support .btn{width:190px;margin-top:24px}

.site-footer{height:72px;background:var(--black);display:flex;align-items:center;justify-content:center;color:var(--dim-text);font-size:11px}
</style>
</head>
<body>
<header class="site-header">
  <div class="brand"><span class="brand-mark"></span>Golden Years Mobile Massage</div>
  <nav class="main-nav">
    <a href="#">HOME</a>
    <a href="#">MASSAGE SERVICES</a>
    <a href="#">CONTACT US</a>
    <a href="#">ホーム</a>
    <span class="search-btn"><svg width="14" height="14" viewBox="0 0 14 14"><circle cx="6" cy="6" r="4.2" fill="none" stroke="#9ccb3b" stroke-width="2"/><line x1="9" y1="9" x2="12.5" y2="12.5" stroke="#9ccb3b" stroke-width="2.2"/></svg></span>
  </nav>
</header>

<section class="hero" role="img" aria-label="Photo of a relaxed woman receiving a shoulder massage"></section>

<section class="features">
  <article class="feature-card light" role="img" aria-label="Faded photo of a massage therapist">
    <p class="eyebrow">Golden Years Mobile Massage</p>
    <h2 class="feature-title">LOREM IPSUM DOLOR</h2>
    <p class="feature-text">Lorem ipsum dolor sit amet, consectetur adipisicing elit, sed do eiusmod tempor incididunt ut labore et dolore magna aliqua. Ut ad minim.</p>
    <a class="btn" href="#">View Services</a>
  </article>
  <article class="feature-card dark">
    <p class="eyebrow">Golden Years Mobile Massage</p>
    <h2 class="feature-title">LOREM IPSUM DOLOR</h2>
    <p class="feature-text">Lorem ipsum dolor sit amet, consectetur adipisicing elit, sed do eiusmod tempor incididunt ut labore et dolore magna aliqua. Ut ad minim.</p>
    <a class="btn" href="#">View Services</a>
  </article>
  <article class="feature-card light" role="img" aria-label="Faded photo of a massage therapist">
    <p class="eyebrow">Golden Years Mobile Massage</p>
    <h2 class="feature-title">LOREM IPSUM DOLOR</h2>
    <p class="feature-text">Lorem ipsum dolor sit amet, consectetur adipisicing elit, sed do eiusmod tempor incididunt ut labore et dolore magna aliqua. Ut ad minim.</p>
    <a class="btn" href="#">View Services</a>
  </article>
</section>

<section class="services">
  <p class="eyebrow">Massage Services</p>
  <h2 class="section-title">WHAT WE DO</h2>
  <div class="rule"></div>
  <div class="service-grid">
    <div class="service">
      <div class="service-photo" role="img" aria-label="Photo of an outdoor back massage on a garden lawn"></div>
      <h3 class="service-name">"Lorem Ispum Incididunt"</h3>
      <p class="service-text">Praesent Luptatum Sit amet consectetur adipisicing elit sed do eiusmod tempor incididunt ut labore incididunt ut labore et dolore magna</p>
    </div>
    <div class="service">
      <div class="service-photo" role="img" aria-label="Photo of an outdoor back massage on a garden lawn"></div>
      <h3 class="service-name">"Lorem Ispum Incididunt"</h3>
      <p class="service-text">Praesent Luptatum Sit amet consectetur adipisicing elit sed do eiusmod tempor incididunt ut labore incididunt ut labore et dolore magna</p>
    </div>
    <div class="service">
      <div class="service-photo" role="img" aria-label="Photo of an outdoor back massage on a garden lawn"></div>
      <h3 class="service-name">"Lorem Ispum Incididunt"</h3>
      <p class="service-text">Praesent Luptatum Sit amet consectetur adipisicing elit sed do eiusmod tempor incididunt ut labore incididunt ut labore et dolore magna</p>
    </div>
  </div>
</section>

<section class="contact-head">
  <p class="eyebrow">Contact Us</p>
  <h2 class="section-title">GET IN TOUCH</h2>
  <div class="rule"></div>
</section>

<section class="contact-split">
  <div class="contact-info">
    <p class="eyebrow">For General Questions</p>
    <h2 class="feature-title">CONTACT INFORMATION</h2>
    <p class="lead">Lorem ipsum dolor sit amet, consetetur sadipscing elitr, sed diam nonumy eirmod tempor invidunt ut labore et dolore magna aliquyam erat.</p>
    <p>Phone: <strong>0400-123-456</strong></p>
    <p style="margin-top:8px">Email: <strong>hello@goldenyearsmm.com</strong></p>
  </div>
  <div class="quick-support">
    <p class="eyebrow">Do You Need Us?</p>
    <h2 class="feature-title">QUICK SUPPORT</h2>
    <p>We are Mobile. Call Whenever, Wherever.</p>
    <a class="btn" href="#">Make a Booking Now!</a>
  </div>
</section>

<footer class="site-footer">Copyright © 2016 – Golden Years Mobile Massage. All Right Reserved.</footer>
</body>
</html>
```